Pelton Mortgage Capital Business Card

We need a business card design for our mortgage servicing company. In addition to servicing the loans of homeowners, we help homeowners with purchasing their homes and any mortgage refinancing. We would like to see designs that use the colors in the logo attached below (gold-ish yellow and navy blue), and any other design you deem fit! The design should communicate a simpler life with smart mortgages provided by Pelton.

```html
<!DOCTYPE html>
<html lang="en">
<head>
<meta charset="utf-8">
<title>Pelton Mortgage Capital – Business Card</title>
<link href="https://fonts.googleapis.com/css2?family=Lato:wght@400;700;900&display=swap" rel="stylesheet">
<style>
  :root {
    --navy: #231f55;
    --gold: #e2a92a;
    --paper: #ffffff;
    --ink-soft: #5d5d66;
    --rule-navy: #8b88ad;
    --stage: #2b2c30;
  }
  * { box-sizing: border-box; margin: 0; padding: 0; }
  html, body {
    width: 1200px; height: 952px; overflow: hidden;
    background: var(--stage);
    font-family: "Lato", Arial, sans-serif;
  }
  .sheet {
    width: 1200px; height: 952px;
    display: flex; align-items: center; justify-content: center; gap: 50px;
  }
  .card {
    position: relative;
    width: 540px; height: 310px;
    border-radius: 22px;
    overflow: hidden;
  }
  .card--front { background: var(--paper); color: var(--navy); }
  .card--back { background: var(--navy); color: var(--gold); }

  .wordmark {
    position: absolute; left: 0; right: 0;
    display: flex; align-items: center; justify-content: center; gap: 12px;
    font-weight: 900; font-size: 38px; letter-spacing: 0.5px;
    color: var(--gold);
  }
  .wordmark__dot {
    width: 16px; height: 16px; border-radius: 50%;
    background: var(--gold);
  }
  .card--front .wordmark { top: 62px; }
  .card--back .wordmark { top: 92px; }

  .identity {
    position: absolute; left: 0; top: 176px; width: 250px;
  }
  .identity__name {
    padding-left: 34px;
    font-weight: 700; font-size: 17px; letter-spacing: 0.6px;
    text-transform: uppercase;
  }
  .identity__name .surname { color: var(--gold); }
  .identity__rule {
    height: 1px; background: var(--rule-navy); margin: 7px 0 6px;
  }
  .identity__title {
    padding-left: 60px;
    font-size: 13px; color: var(--ink-soft);
  }

  .contacts {
    position: absolute; left: 270px; top: 172px;
    list-style: none;
    font-size: 12.5px; color: var(--ink-soft);
  }
  .contacts li { display: flex; align-items: center; gap: 9px; margin-bottom: 9px; }
  .contacts svg { width: 16px; height: 16px; flex: none; }

  .address {
    position: absolute; left: 0; right: 0; top: 178px;
    display: flex; align-items: center; gap: 12px;
  }
  .address__rule { flex: 1; height: 1px; background: var(--gold); opacity: 0.7; }
  .address__text {
    text-align: center; font-size: 12px; line-height: 1.45; color: var(--gold);
  }
</style>
</head>
<body>
<main class="sheet">

  <section class="card card--front" aria-label="Business card front">
    <div class="wordmark"><span class="wordmark__dot"></span>Pelton Mortgage</div>

    <div class="identity">
      <p class="identity__name">Daniel R. <span class="surname">Whitford</span></p>
      <div class="identity__rule"></div>
      <p class="identity__title">Managing Director</p>
    </div>

    <ul class="contacts">
      <li>
        <svg viewBox="0 0 16 16" aria-hidden="true"><rect width="16" height="16" rx="3" fill="#e2a92a"/><path d="M5.2 3.6l1.6 2.1-1 1c.5 1.3 1.4 2.2 2.6 2.7l1-1 2.1 1.6-1 1.6c-3.4-.2-6-2.9-6.3-6.3z" fill="#fff"/></svg>
        +00 987 654 32
      </li>
      <li>
        <svg viewBox="0 0 16 16" aria-hidden="true"><rect width="16" height="16" rx="3" fill="#e2a92a"/><rect x="3.5" y="5" width="9" height="6.4" fill="none" stroke="#fff" stroke-width="1.2"/><path d="M3.5 5l4.5 3.6L12.5 5" fill="none" stroke="#fff" stroke-width="1.2"/></svg>
        hello@peltonmortgage.com
      </li>
      <li>
        <svg viewBox="0 0 16 16" aria-hidden="true"><rect width="16" height="16" rx="3" fill="#e2a92a"/><path d="M5 3.5l6.5 5-3 .4 1.7 3.2-1.2.6-1.7-3.2-2.2 2z" fill="#fff"/></svg>
        www.peltonmortgage.com
      </li>
    </ul>
  </section>

  <section class="card card--back" aria-label="Business card back">
    <div class="wordmark"><span class="wordmark__dot"></span>Pelton Mortgage</div>
    <div class="address">
      <span class="address__rule"></span>
      <p class="address__text">2170 Harbor View Avenue Annapolis<br>MD 21401</p>
      <span class="address__rule"></span>
    </div>
  </section>

</main>
</body>
</html>
```